Red Gum Business Card Design

We are a new small business specialising in under ground cable jointing and excavation works in NSW Australia.
Design I'm looking for is incorporating the Australian flag & excavator with out being to cheesy.
Maybe a faded washed out flag to help with overload of colour? & so its not the main focus.
Very open to creative out of the box designs!

Target Market(s)

Building & Construction

Industry/Entity Type

Construction

Contact Information for Business Card

Red Gum Cable Jointing & Excavations
Owen Falkirk

Ph: 0438 605 312
E: owen.falkirk@tallmail.example

Reverse Side
Services we offer:
High Voltage & Low Voltage Cable Jointing
Polymeric & paperlead jointing & terminations
Trenching & Auger Drilling 150 - 600mm
Site preparation / leveling / clearing
Driveway / Footpath / Turf Prep
Rubbish Removal
Tree & Stump removal
Footings & Post holes
Drainage
Service Installs
Gravels & Sands available
Any general Earth moving needs
Reliable Free Quotes
Fully Insured

Font styles to use
Serif
Script

Requirements
Nice to have
• small excavator (See uploaded picture)

```html
<!DOCTYPE html>
<html lang="en">
<head>
<meta charset="utf-8">
<title>Red Gum Business Card Design</title>
<link rel="stylesheet" href="https://fonts.googleapis.com/css2?family=Merriweather:ital,wght@0,400;0,700;1,300&family=Merriweather+Sans:wght@400&display=swap">
<style>
  :root {
    --backdrop: #b4b4b6;
    --card-white: #ffffff;
    --card-grey: #9d9b9a;
    --ink: #1c1c1c;
    --ink-soft: #2e2e2e;
    --rule: #3a3a3a;
    --star-tone: rgba(255,255,255,0.55);
  }
  * { box-sizing: border-box; margin: 0; padding: 0; }
  html, body { width: 1200px; height: 780px; overflow: hidden; }
  body { background: var(--backdrop); position: relative; font-family: "Merriweather", serif; color: var(--ink); }

  .card {
    position: absolute;
    width: 470px;
    height: 282px;
    overflow: hidden;
    box-shadow: 0 2px 6px rgba(0,0,0,0.18);
    background: var(--card-grey);
  }

  /* Front */
  .card--front { left: 82px; top: 92px; }
  .front__top { position: absolute; inset: 0 0 auto 0; height: 132px; background: var(--card-white); }
  .brand { position: absolute; left: 46px; top: 42px; }
  .brand__name { font-weight: 700; font-size: 27px; letter-spacing: 1px; line-height: 1; color: var(--ink); }
  .brand__tagline { font-weight: 700; font-size: 10.5px; letter-spacing: 0.4px; margin-top: 4px; color: var(--ink); }
  .excavator-art {
    position: absolute; left: 292px; top: 74px; width: 150px; height: 190px;
    background: linear-gradient(160deg, #2a2a2a, #0d0d0d);
    border-radius: 4px;
  }
  .holder { position: absolute; left: 46px; top: 164px; }
  .holder__name { font-style: italic; font-weight: 300; font-size: 22px; letter-spacing: 1px; color: var(--ink-soft); text-transform: uppercase; }
  .contact { list-style: none; margin-top: 14px; font-family: "Merriweather Sans", sans-serif; font-size: 13px; color: var(--ink); }
  .contact li { display: flex; align-items: center; gap: 8px; line-height: 21px; }
  .contact svg { width: 12px; height: 12px; flex: none; }

  /* Back */
  .card--back { left: 624px; top: 426px; }
  .back__top { position: absolute; inset: 0 0 auto 0; height: 40px; background: var(--card-white); border-bottom: 2px solid var(--rule); }
  .services__title { position: absolute; top: 21px; width: 100%; text-align: center; font-size: 12px; letter-spacing: 0.3px; }
  .star-field {
    position: absolute; left: 40px; top: 20px; width: 430px; height: 262px;
    background: radial-gradient(ellipse at 70% 55%, var(--star-tone), rgba(255,255,255,0) 65%);
  }
  .services { position: absolute; top: 50px; width: 100%; list-style: none; text-align: center; font-size: 9.6px; line-height: 14.2px; text-transform: uppercase; color: var(--ink); }
  .services li::before { content: "• "; }
  .services .services__insured { font-weight: 700; }
</style>
</head>
<body>
  <section class="card card--front" aria-label="Business card front">
    <div class="front__top"></div>
    <div class="brand">
      <div class="brand__name">RED GUM</div>
      <div class="brand__tagline">CABLE JOINTING &amp; EXCAVATIONS</div>
    </div>
    <div class="excavator-art" role="img" aria-label="Black silhouette of a small excavator"></div>
    <div class="holder">
      <div class="holder__name">Owen Falkirk</div>
      <ul class="contact">
        <li>
          <svg viewBox="0 0 24 24" aria-hidden="true"><path fill="#1c1c1c" d="M6.6 10.8a15.1 15.1 0 0 0 6.6 6.6l2.2-2.2c.3-.3.7-.4 1-.2 1.1.4 2.3.6 3.6.6.6 0 1 .4 1 1V20c0 .6-.4 1-1 1A17 17 0 0 1 3 4c0-.6.4-1 1-1h3.5c.6 0 1 .4 1 1 0 1.3.2 2.5.6 3.6.1.3 0 .7-.2 1z"/></svg>
          0438 605 312
        </li>
        <li>
          <svg viewBox="0 0 24 24" aria-hidden="true"><rect x="2" y="5" width="20" height="14" fill="none" stroke="#1c1c1c" stroke-width="2"/><path d="M2 6l10 7 10-7" fill="none" stroke="#1c1c1c" stroke-width="2"/></svg>
          owen.falkirk@tallmail.example
        </li>
      </ul>
    </div>
  </section>

  <section class="card card--back" aria-label="Business card back">
    <div class="star-field" role="img" aria-label="Faint white Southern Cross stars"></div>
    <div class="back__top"></div>
    <h2 class="services__title" style="font-weight:400">SERVICES WE OFFER:</h2>
    <ul class="services">
      <li>High Voltage &amp; Low Voltage Cable Jointing</li>
      <li>Polymeric &amp; Paperlead Jointing &amp; Terminations</li>
      <li>Trenching &amp; Auger Drilling 150 - 600mm</li>
      <li>Site Preparation / Leveling / Clearing</li>
      <li>Driveway / Footpath / Turf Prep</li>
      <li>Rubbish Removal</li>
      <li>Tree &amp; Stump Removal</li>
      <li>Footings &amp; Post Holes</li>
      <li>Drainage</li>
      <li>Service Installs</li>
      <li>Gravels &amp; Sands Available</li>
      <li>Any General Earth Moving Needs</li>
      <li>Reliable Free Quotes</li>
      <li class="services__insured">Fully Insured</li>
    </ul>
  </section>
</body>
</html>
```